PowerPoint Template for our Business

We are looking for a professional and visually appealing PowerPoint template for our business, Pellion Labs. We specialize in calibration services and are currently undergoing a rebranding process. The new template should align with our updated brand identity, using the provided color palette and logos.
Project Requirements:
Title Slide:
Full Pellion Labs logo prominently displayed.
Clean and professional layout.
Background color should be white with brand accents.
Title and subtitle areas clearly defined.
Content Slide:
Consistent use of brand colors for headers, footers, and other elements.
Space for text, images, charts, and graphs.
PX logo subtly incorporated.
Clean and modern layout ensuring readability and professionalism.
Section Header Slide:
Clear differentiation from content slides.
Use of PX logo and brand color for background.
Professional typography.
Closing Slide:
Full Pellion Labs logo with a final message.
Clean background, professional layout.
Space for a thank you message and contact information.
Brand Colors:
Green: RGB (207, 255, 0)
Light Gray: RGB (239, 239, 239)
Gray: RGB (191, 191, 191)
Black: RGB (0, 0, 0)
White: RGB (255, 255, 255)
Deliverables:
A fully editable PowerPoint template (.pptx format).
Fonts and any additional assets used in the design.
Additional Information:
Please refer to the attached logos and color palette for guidance.
We are looking for a design that is not only professional and visually appealing but also functional for business presentations.
We look forward to seeing your creative proposals and selecting a design that best represents our brand.
Thank you!

```html
<!DOCTYPE html>
<html lang="en">
<head>
<meta charset="utf-8">
<title>Pellion Labs – Presentation Template</title>
<link href="https://fonts.googleapis.com/css2?family=Outfit:wght@300;400;500;800&display=swap" rel="stylesheet">
<style>
  :root{
    --brand-green:#cfff00;
    --light-gray:#efefef;
    --gray:#bfbfbf;
    --mid-gray:#8a8a8a;
    --dark-gray:#555555;
    --black:#000000;
    --white:#ffffff;
    --board:#8dabd5;
  }
  *{margin:0;padding:0;box-sizing:border-box}
  html,body{width:1200px;height:747px;overflow:hidden}
  body{background:var(--board);font-family:"Outfit",sans-serif;color:var(--black);position:relative}
  .slide{position:absolute;width:523px;height:294px;background:var(--white);overflow:hidden;
    box-shadow:0 14px 14px -8px rgba(30,45,70,.45)}
  .slide--title{left:58px;top:60px}
  .slide--content{left:619px;top:60px}
  .slide--section{left:58px;top:392px}
  .slide--closing{left:619px;top:392px}
  .abs{position:absolute}
  .sparkles{position:absolute;inset:0;pointer-events:none}
  .spark-green{fill:var(--brand-green)}
  .spark-black{fill:var(--black)}

  /* wordmark */
  .brand-square{position:absolute;background:var(--black)}
  .wordmark{position:absolute;font-weight:400;color:var(--black);white-space:nowrap;line-height:1}

  /* title slide */
  .title-slide__square{left:29px;top:40px;width:53px;height:53px}
  .title-slide__wordmark{left:94px;top:53px;font-size:24px}
  .title-slide__title{left:24px;top:130px;width:185px;height:70px;background:var(--brand-green);
    font-weight:800;font-size:30px;line-height:28px;padding:7px 0 0 14px}
  .title-slide__subtitle{left:33px;top:193px;width:190px;height:64px;background:var(--black);color:var(--white);
    font-size:19px;line-height:23px;padding:10px 0 0 9px;transform:rotate(-1.5deg);font-weight:400}
  .title-slide__photo{left:282px;top:26px;width:241px;height:229px;
    background:radial-gradient(circle at 55% 40%,#e2a73d 0%,#8a5a1c 30%,#2a2620 62%,#101820 100%)}

  /* content slide */
  .content__accent{left:19px;top:19px;width:4px;height:127px;background:var(--brand-green)}
  .content__kicker{left:36px;top:21px;font-size:15px;letter-spacing:2.6px;color:var(--mid-gray);font-weight:500}
  .content__heading{left:36px;top:41px;font-size:21px;font-weight:800}
  .content__body{left:36px;top:73px;width:190px;font-size:9.6px;line-height:11.8px;font-weight:400}
  .content__photo{left:299px;top:17px;width:199px;height:106px;
    background:linear-gradient(100deg,#6b3a2a 0%,#c24a22 28%,#3b3f48 55%,#cfd3d8 80%,#2a6fd6 100%)}
  .info-card{position:absolute;top:181px;width:129px;height:91px;padding:5px 8px;font-size:9.6px;line-height:11.8px}
  .info-card__title{font-size:11.5px;font-weight:500;margin-bottom:5px}
  .info-card--tinted{left:19px;background:var(--light-gray);border:1px solid var(--brand-green);color:var(--mid-gray)}
  .info-card--outline{left:158px;border:1px solid var(--dark-gray);color:var(--mid-gray)}
  .info-card--outline .info-card__title,.info-card--tinted .info-card__title{color:var(--dark-gray)}
  .content__chart{left:333px;top:135px;width:166px;height:137px;background:var(--light-gray)}
  .chart-label{font-family:"Outfit",sans-serif;font-size:7px;fill:var(--gray)}

  /* section slide */
  .section__band{left:0;top:91px;width:523px;height:54px;background:var(--brand-green)}
  .section__strip{left:0;top:145px;width:523px;height:61px;background:var(--black)}
  .section__title{right:150px;top:100px;font-size:30px;font-weight:800;line-height:36px;white-space:nowrap}
  .section__subtitle{left:142px;top:152px;width:240px;text-align:center;color:var(--white);font-size:19px;line-height:23px}
  .section__photo{left:384px;top:17px;width:126px;height:188px;border-radius:14px;
    background:linear-gradient(160deg,#f6b62b 0%,#e99a10 30%,#3a3a3a 45%,#2b2b2b 85%,#f0a81c 100%)}

  /* closing slide */
  .closing__square{left:42px;top:70px;width:44px;height:44px}
  .closing__wordmark{left:97px;top:82px;font-size:21px}
  .closing__divider{left:262px;top:59px;width:1px;height:180px;background:var(--gray)}
  .contact-list{position:absolute;left:42px;top:132px;list-style:none;font-size:10px;line-height:12px}
  .contact-list li{display:flex;align-items:flex-start;gap:8px;margin-bottom:6px}
  .contact-list svg{flex:none;width:9px;height:10px;margin-top:1px}
  .closing__thanks{left:276px;top:79px;font-size:21px;font-weight:800;white-space:nowrap}
  .closing__thanks-mark{display:inline-block;width:5px;height:27px;background:var(--brand-green);vertical-align:-6px;margin-left:1px;transform:skewX(-6deg)}
  .closing__text{left:276px;width:205px;font-size:9.6px;line-height:11.8px}
  .closing__text--one{top:120px}
  .closing__text--two{top:164px}
</style>
</head>
<body>
<svg width="0" height="0" style="position:absolute">
  <defs>
    <symbol id="sparkle" viewBox="-6 -6 12 12">
      <path d="M0,-6 L1.4,-1.4 L6,0 L1.4,1.4 L0,6 L-1.4,1.4 L-6,0 L-1.4,-1.4Z"/>
    </symbol>
  </defs>
</svg>

<!-- Title slide -->
<section class="slide slide--title">
  <div class="abs title-slide__photo" role="img" aria-label="Close-up photo of a precision measuring instrument in warm amber light"></div>
  <div class="brand-square title-slide__square"></div>
  <div class="wordmark title-slide__wordmark">Pellion Labs</div>
  <h1 class="abs title-slide__title">Pellion<br>Labs</h1>
  <p class="abs title-slide__subtitle">Lorem Ipsum dolor<br>sit lorem ipsum</p>
  <svg class="sparkles" viewBox="0 0 523 294">
    <use href="#sparkle" class="spark-green" x="103" y="21" width="14" height="14"/>
    <use href="#sparkle" class="spark-black" x="301" y="85" width="14" height="14"/>
    <use href="#sparkle" class="spark-green" x="401" y="253" width="14" height="14"/>
    <rect x="14" y="262" width="2.5" height="14" class="spark-black" transform="rotate(-20 15 269)"/>
    <rect x="10" y="268" width="2.5" height="14" class="spark-green" transform="rotate(-20 11 275)"/>
  </svg>
</section>

<!-- Content slide -->
<section class="slide slide--content">
  <div class="abs content__accent"></div>
  <p class="abs content__kicker">Pellion Labs</p>
  <h2 class="abs content__heading">Pellion Labs</h2>
  <p class="abs content__body">Lorem ipsum dolor sit amet, consectetur adipiscing elit, sed do eiusmod tempor incididunt ut labore et dolore magna aliqua. Quis ipsum suspendisse ultrices gravida. Risus commodo viverra maecenas accumsan lacus vel facilisis.</p>
  <div class="abs content__photo" role="img" aria-label="Photo of a technician calibrating industrial pipe gauges"></div>
  <div class="info-card info-card--tinted">
    <p class="info-card__title">Pellion Labs</p>
    <p>Lorem ipsum dolor sit amet, consectetur adipiscing elit, sed do eiusmod tempor incididunt ut labore</p>
  </div>
  <div class="info-card info-card--outline">
    <p class="info-card__title">Pellion Labs</p>
    <p>Lorem ipsum dolor sit amet, consectetur adipiscing elit, sed do eiusmod tempor incididunt ut</p>
  </div>
  <svg class="abs content__chart" viewBox="0 0 166 137" role="img" aria-label="Bar chart">
    <g class="chart-labels">
      <text class="chart-label" x="8" y="23">60</text>
      <text class="chart-label" x="8" y="42">50</text>
      <text class="chart-label" x="8" y="61">40</text>
      <text class="chart-label" x="8" y="80">30</text>
      <text class="chart-label" x="8" y="99">20</text>
      <text class="chart-label" x="8" y="118">10</text>
    </g>
    <line x1="22" y1="11" x2="22" y2="126" stroke="#bfbfbf" stroke-width="1.2"/>
    <line x1="22" y1="126" x2="157" y2="126" stroke="#bfbfbf" stroke-width="1.2"/>
    <g stroke-linecap="round" stroke-width="7">
      <line x1="35" y1="67" x2="35" y2="118" stroke="#555"/>
      <line x1="44" y1="30" x2="44" y2="118" stroke="#cfff00"/>
      <line x1="55" y1="50" x2="55" y2="118" stroke="#bfbfbf"/>
      <line x1="73" y1="67" x2="73" y2="118" stroke="#555"/>
      <line x1="82" y1="30" x2="82" y2="118" stroke="#cfff00"/>
      <line x1="93" y1="50" x2="93" y2="118" stroke="#bfbfbf"/>
      <line x1="111" y1="67" x2="111" y2="118" stroke="#555"/>
      <line x1="120" y1="30" x2="120" y2="118" stroke="#cfff00"/>
      <line x1="131" y1="50" x2="131" y2="118" stroke="#bfbfbf"/>
      <line x1="142" y1="67" x2="142" y2="118" stroke="#555"/>
    </g>
  </svg>
</section>

<!-- Section header slide -->
<section class="slide slide--section">
  <div class="abs section__band"></div>
  <div class="abs section__strip"></div>
  <h2 class="abs section__title">Pellion Labs</h2>
  <p class="abs section__subtitle">Lorem Ipsum dolor sit<br>lorem ipsum</p>
  <div class="abs section__photo" role="img" aria-label="Photo of a yellow handheld digital multimeter"></div>
  <svg class="sparkles" viewBox="0 0 523 294">
    <use href="#sparkle" class="spark-green" x="41" y="29" width="14" height="14"/>
    <use href="#sparkle" class="spark-black" x="245" y="39" width="14" height="14"/>
    <use href="#sparkle" class="spark-green" x="401" y="224" width="14" height="14"/>
    <use href="#sparkle" fill="#e4e4e4" x="22" y="258" width="14" height="14"/>
    <rect x="134" y="227" width="14" height="2.5" class="spark-black" transform="rotate(25 141 228)"/>
    <rect x="134" y="233" width="14" height="2.5" class="spark-green" transform="rotate(25 141 234)"/>
    <rect x="474" y="256" width="2.5" height="14" class="spark-black" transform="rotate(-20 475 263)"/>
    <rect x="470" y="262" width="2.5" height="14" class="spark-green" transform="rotate(-20 471 269)"/>
  </svg>
</section>

<!-- Closing slide -->
<section class="slide slide--closing">
  <div class="brand-square closing__square"></div>
  <div class="wordmark closing__wordmark">Pellion Labs</div>
  <ul class="contact-list">
    <li>
      <svg viewBox="0 0 10 12"><path d="M5 0a4 4 0 0 0-4 4c0 3 4 8 4 8s4-5 4-8a4 4 0 0 0-4-4zm0 5.6a1.6 1.6 0 1 1 0-3.2 1.6 1.6 0 0 1 0 3.2z"/></svg>
      <span>Lorem ipsum dolor sit amet,<br>consectetur adipiscing elit</span>
    </li>
    <li>
      <svg viewBox="0 0 12 12"><path d="M2.5 0.5l2 2.3-1.2 1.6c.8 1.7 2 2.9 3.6 3.7l1.6-1.2 2.3 2-1.3 2.4C5 11 1 7 .3 1.8z"/></svg>
      <span>+1 555 014 2386</span>
    </li>
    <li>
      <svg viewBox="0 0 12 10"><path d="M0 1h12v8H0z M0 1l6 4 6-4" fill="#000" stroke="#fff" stroke-width=".9"/></svg>
      <span>info@pellionlabs.com</span>
    </li>
    <li>
      <svg viewBox="0 0 10 12"><path d="M1 0v10l2.5-2.3 1.8 4 1.6-.7-1.8-3.9H8.5z"/></svg>
      <span>www.pellionlabs.com</span>
    </li>
  </ul>
  <div class="abs closing__divider"></div>
  <h2 class="abs closing__thanks">Thank You<span class="closing__thanks-mark"></span></h2>
  <p class="abs closing__text closing__text--one">Lorem ipsum dolor sit amet, consectetur adipiscing elit, sed do eiusmod tempor incididunt ut labore et dolore magna aliqua.</p>
  <p class="abs closing__text closing__text--two">Lorem ipsum dolor sit amet, consectetur adipiscing elit, sed do eiusmod tempor incididunt ut labore et dolore magna aliqua.</p>
  <svg class="sparkles" viewBox="0 0 523 294">
    <use href="#sparkle" class="spark-black" x="439" y="36" width="15" height="15"/>
    <use href="#sparkle" class="spark-green" x="203" y="251" width="15" height="15"/>
  </svg>
</section>
</body>
</html>
```